Nine Moons Brochure Design Project

I need a brochure for my new company "Nine Moons". You can read all about the company at http://www.ninemoons-example.com.sg
On the website you will also get an idea of the concept of the product, as well as design. This design actually comes from a Wordpress theme.
The brochure needs to be like a print version of the website but much more summarised, high-level. I'd like to distribute it to expecting mothers at various locations such as pre-natal yoga classes. The intention is to create enough interest so these moms-to-be will surf to my website and check out what it's all about.
Target Market(s)
Expecting moms and dads (pregnant)
Industry/Entity Type
It Company
Look and feel

```html
<!DOCTYPE html>
<html lang="en">
<head>
<meta charset="utf-8">
<title>Nine Moons Brochure</title>
<link href="https://fonts.googleapis.com/css2?family=Oswald:wght@300;400&family=Raleway:wght@300;400;600;700&display=swap" rel="stylesheet">
<style>
  :root {
    --backdrop: #e8e5e1;
    --paper: #ffffff;
    --teal: #6cc6ca;
    --teal-deep: #4eaeb3;
    --teal-dark: #3b959a;
    --ink: #8b9397;
    --ink-dark: #5f676b;
    --ink-soft: #a9b0b3;
  }
  * { box-sizing: border-box; margin: 0; padding: 0; }
  html, body { width: 1200px; height: 804px; overflow: hidden; }
  body {
    background: var(--backdrop);
    font-family: "Raleway", Arial, sans-serif;
    color: var(--ink);
    position: relative;
  }
  .page {
    position: absolute;
    top: 147px;
    width: 360px;
    height: 510px;
    background: var(--paper);
    box-shadow: 0 6px 18px rgba(0,0,0,.12);
    overflow: hidden;
  }

  /* Cover */
  .cover {
    left: 40px;
    background: linear-gradient(160deg, #ffffff 0%, #f3f5f6 60%, #e4e8ea 100%);
  }
  .cover-photo {
    position: absolute;
    left: 20px; top: 18px;
    width: 166px; height: 420px;
    border-radius: 40px 40px 10px 10px;
    background: linear-gradient(180deg, #d9c3b2 0%, #efe9e4 35%, #f6f6f6 70%, #e9ebec 100%);
  }
  .cover-headline {
    position: absolute;
    left: 196px; top: 120px;
    width: 150px;
    text-align: center;
    font-family: "Oswald", "Arial Narrow", sans-serif;
    font-weight: 400;
    text-transform: uppercase;
    color: var(--ink);
    font-size: 15px;
    line-height: 1.35;
    letter-spacing: .4px;
  }
  .cover-headline .relax {
    display: block;
    font-size: 25px;
    letter-spacing: 2px;
    margin-bottom: 4px;
  }
  .cover-brand {
    position: absolute;
    right: 42px; top: 410px;
    font-weight: 600;
    font-size: 16px;
    color: var(--ink-dark);
  }
  .ribbon { position: relative; display: block; flex: none; }
  .ribbon svg { display: block; }
  .ribbon-label {
    position: absolute;
    color: #fff;
    text-transform: uppercase;
    font-family: "Oswald", "Arial Narrow", sans-serif;
    white-space: nowrap;
  }
  .cover-ribbon { position: absolute; left: 10px; top: 446px; width: 340px; height: 40px; }
  .cover-ribbon .ribbon-label {
    left: 0; right: 0; top: 11px;
    text-align: center;
    font-size: 11.5px;
    letter-spacing: .6px;
  }

  /* Spread */
  .spread-left { left: 440px; }
  .spread-right { left: 800px; }
  .spread-left::after {
    content: "";
    position: absolute; top: 0; right: 0;
    width: 28px; height: 100%;
    background: linear-gradient(90deg, rgba(0,0,0,0), rgba(0,0,0,.07));
  }
  .spread-right::before {
    content: "";
    position: absolute; top: 0; left: 0;
    width: 28px; height: 100%;
    background: linear-gradient(90deg, rgba(0,0,0,.07), rgba(0,0,0,0));
  }
  .spread-left-flow {
    display: flex;
    flex-direction: column;
    padding-top: 30px;
    height: 100%;
  }
  .intro-ribbon { width: 190px; height: 34px; margin-bottom: 16px; }
  .intro-ribbon .ribbon-label {
    left: 30px; top: 7px;
    font-size: 14px;
    letter-spacing: .5px;
  }
  .body-copy {
    margin-left: 26px; width: 306px;
    font-size: 9.6px;
    line-height: 1.55;
    color: var(--ink);
  }
  .intro-copy p + p { margin-top: 6px; }
  .subhead {
    margin: 16px 0 12px 26px;
    font-size: 17px;
    font-weight: 300;
    color: var(--teal);
    line-height: 1.2;
  }
  .booties-photo {
    margin-left: 26px;
    width: 306px; height: 124px;
    flex: none;
    background: linear-gradient(90deg, #c4d7e6 0%, #dfe8ef 45%, #f2d6dc 60%, #eab9c3 100%);
    border-radius: 6px;
  }
  .closing-copy { margin-top: 24px; }
  .closing-copy strong { color: var(--ink-dark); font-weight: 700; }

  /* Services */
  .services-column {
    position: absolute;
    left: 24px; top: 22px; width: 172px;
  }
  .services-title {
    font-weight: 700; font-size: 13px;
    letter-spacing: .8px;
    color: var(--ink-dark);
    line-height: 1.2;
  }
  .services-phase {
    font-size: 13px; font-weight: 400;
    color: var(--teal);
    line-height: 1.3;
    margin: 4px 0 8px;
  }
  .phase-birth { margin-top: 4px; }
  .service-list {
    list-style: none;
    font-size: 9px;
    color: var(--ink);
  }
  .service-list li {
    position: relative;
    padding-left: 15px;
    margin-bottom: 9px;
    line-height: 1.3;
    white-space: nowrap;
  }
  .service-list li::before {
    content: "";
    position: absolute; left: 0; top: 2px;
    width: 7px; height: 7px;
    background: var(--teal);
  }
  .list-side { position: absolute; left: 198px; top: 24px; width: 150px; }
  .list-side li { white-space: normal; }

  .contact {
    position: absolute;
    left: 184px; top: 224px; width: 170px;
    text-align: center;
  }
  .contact-lead { font-size: 9px; color: var(--teal); font-weight: 600; }
  .contact-web { font-size: 10.5px; color: var(--ink-soft); font-weight: 600; margin-top: 8px; white-space: nowrap; }
  .contact-or { font-size: 9px; color: var(--teal); font-weight: 600; margin-top: 2px; }
  .contact-phone { font-size: 20px; color: var(--teal); font-weight: 600; margin-top: 8px; letter-spacing: .5px; }

  .meet-panel {
    position: absolute;
    left: 16px; top: 360px;
    width: 334px; height: 122px;
    background: var(--teal);
  }
  .meet-photo {
    position: absolute;
    left: 12px; top: 12px;
    width: 82px; height: 98px;
    border: 4px solid #fff;
    background: linear-gradient(180deg, #e7e1dc, #f6f4f2);
  }
  .meet-title {
    position: absolute; left: 108px; top: 10px;
    font-family: "Oswald", "Arial Narrow", sans-serif;
    font-weight: 400;
    font-size: 15px; color: #fff;
    letter-spacing: .6px;
  }
  .meet-copy {
    position: absolute; left: 108px; top: 36px; width: 216px;
    font-size: 8.4px; line-height: 1.45; color: #fff;
  }
</style>
</head>
<body>

  <section class="page cover">
    <div class="cover-photo" role="img" aria-label="Photo of a pregnant woman in a white top holding her belly"></div>
    <h1 class="cover-headline">
      <span class="relax">...Relax...</span>
      And let us take care of planning, organising and preparing for the arrival of your little one!
    </h1>
    <div class="cover-brand">Nine Moons</div>
    <div class="ribbon cover-ribbon">
      <svg width="340" height="40" viewBox="0 0 340 40">
        <polygon points="0,10 30,10 30,34 0,34 10,22" fill="var(--teal-deep)"/>
        <polygon points="340,10 310,10 310,34 340,34 330,22" fill="var(--teal-deep)"/>
        <polygon points="20,34 30,34 30,40" fill="var(--teal-dark)"/>
        <polygon points="320,34 310,34 310,40" fill="var(--teal-dark)"/>
        <rect x="20" y="4" width="300" height="30" fill="var(--teal)"/>
      </svg>
      <span class="ribbon-label">Personalised Baby Planner &amp; Maternity Concierge</span>
    </div>
  </section>

  <section class="page spread-left">
    <div class="spread-left-flow">
      <div class="ribbon intro-ribbon">
        <svg width="190" height="34" viewBox="0 0 190 34">
          <polygon points="0,0 190,0 178,17 190,34 0,34" fill="var(--teal)"/>
        </svg>
        <span class="ribbon-label">You're expecting!</span>
      </div>
      <div class="body-copy intro-copy">
        <p>Joyful news awaits you at the end of nine months, and a mountain of questions is already piling up in anticipation of your little one. Questions your doctor or midwife just can't answer.</p>
        <p>What to buy to prepare for this baby? Essential vs. nice to have? Who will plan the baby shower? How should I decorate the nursery? What about a confinement nanny and the first-month celebration? Have I selected a birth plan? I need to start researching hospitals...</p>
      </div>
      <h2 class="subhead">So much to do and think about!</h2>
      <div class="booties-photo" role="img" aria-label="Photo of knitted baby booties, one blue pair and one pink pair"></div>
      <div class="body-copy closing-copy">
        <p><strong>Nine Moons</strong> is a Baby Planning &amp; Maternity Concierge that lets busy moms and dads relax while we take care of all the planning. First-time parents are relieved for the guidance, and experienced parents just appreciate the extra set of hands and brains!</p>
      </div>
    </div>
  </section>

  <section class="page spread-right">
    <div class="services-column">
      <h2 class="services-title">SERVICES</h2>
      <h3 class="services-phase">During your pregnancy...</h3>
      <ul class="service-list">
        <li>The Nine Moons Action Plan</li>
        <li>Product reviews and suggestions</li>
        <li>Nursery Setup &amp; Design</li>
        <li>Layette Shopping</li>
        <li>Baby Shower Planning</li>
        <li>Sourcing for Confinement Nanny</li>
        <li>Newborn Care</li>
      </ul>
      <h3 class="services-phase phase-birth">After birth...</h3>
      <ul class="service-list">
        <li>Newborn Care (up to 12 mths)</li>
        <li>Postpartum Support</li>
        <li>Asian Confinement Traditions</li>
        <li>Nanny / Childcare Sourcing</li>
        <li>Baby Food Making</li>
      </ul>
    </div>
    <ul class="service-list list-side">
      <li>Baby Registry Setup</li>
      <li>Birth Planning</li>
      <li>Baby Announcements</li>
      <li>Health, Happiness &amp; Well Being</li>
      <li>Advice &amp; Consultation</li>
      <li>Concierge Service</li>
    </ul>
    <div class="contact">
      <p class="contact-lead">For more informations go to</p>
      <p class="contact-web">www.ninemoons-example.com.sg</p>
      <p class="contact-or">or call me</p>
      <p class="contact-phone">8000-1234</p>
    </div>
    <div class="meet-panel">
      <div class="meet-photo" role="img" aria-label="Photo of a smiling pregnant woman resting in white"></div>
      <h3 class="meet-title">LET'S MEET</h3>
      <p class="meet-copy">The first thing I do is a free telephone or face-to-face consultation at a location of your choice, be that your home, or somewhere we can grab a coffee together. The idea is to get to know you and your pregnancy better, and find out your needs and goals as well as your budget.</p>
    </div>
  </section>

</body>
</html>
```